UK based media owner KELVANO (http://www.kelvano.uk/) needs DIGITAL ADVERT to run on our digital panel

Hi guys,

Thanks for taking the time to have a look at this brief.
I need someone to create a digital advert (still/static design or video) to run on our digital panels which are located across UK university student unions.
For who wants to upload a video ---> All of our panels are digitally enabled and allow for full motion video – they run adverts 10 seconds long (see artwork specification document in attachment) therefore the advert will have to be 10 seconds long.
For static/still design ----> see artwork specification to see resolution etc

I need something professional looking, polished yet fresh and exciting so that it speaks and connects to this younger audience – we want to inspire them to take a step towards new levels of business opportunities.

Here are some Key Points you’ll need to take into consideration when designing the advert:

Overall Campaign Objective: To excite and attract young entrepreneurs to get in touch with us for possible partnerships

Target Audience: Young entrepreneurs attending university (university students – 18 to 24 years old)

Creative Specifications: See attached document with artwork specifications

Text on Advert:

I need the following text to appear on the advert: (Please include company logo)

“Do you have a business idea that would benefit with advertising on these screens?

We want to support young entrepreneurs and will partner with any whom have a great idea

WE WANT TO HEAR FROM YOU!

Email us at ideas@kelvano.uk
www.kelvano.uk/ideas”

I would need some ideas by the 3rd July 2018 if possible.

Thanks to all who will take part in this project – contact me if you have any questions

Target Market(s)

Young entrepreneurs attending university (university students – 18 to 24 years old)

Requirements
Must have
• I need the following text to appear on the advert: (Please include company logo)
• “Do you have a business idea that would benefit with advertising on these screens?
• We want to support young entrepreneurs and will partner with any whom have a great idea
• WE WANT TO HEAR FROM YOU!
• Email us at ideas@kelvano.uk
• www.kelvano.uk/ideas”

```html
<!DOCTYPE html>
<html lang="en">
<head>
<meta charset="utf-8">
<title>KELVANO – Young Entrepreneurs</title>
<link rel="stylesheet" href="https://fonts.googleapis.com/css2?family=Lato:wght@300;400&display=swap">
<style>
  :root {
    --paper: #ececec;
    --panel: #dedede;
    --brand-red: #b20e22;
    --ink: #111111;
    --white: #ffffff;
    --photo-light: #e6e2de;
    --photo-mid: #c9bfb6;
    --photo-dark: #8d7563;
  }
  html, body {
    margin: 0;
    padding: 0;
    overflow: hidden;
    background: var(--paper);
  }
  .advert {
    position: relative;
    width: 675px;
    height: 1200px;
    overflow: hidden;
    background: var(--paper);
    font-family: 'Lato', sans-serif;
    font-weight: 300;
  }
  .backdrop {
    position: absolute;
    inset: 0;
    width: 675px;
    height: 1200px;
  }
  .web-address {
    position: absolute;
    left: 48px;
    top: 58px;
    margin: 0;
    font-size: 21px;
    letter-spacing: 0.5px;
    color: var(--ink);
  }
  .brand-name {
    position: absolute;
    left: 366px;
    top: 40px;
    margin: 0;
    font-weight: 400;
    font-size: 40px;
    letter-spacing: 14px;
    color: var(--white);
  }
  .question {
    position: absolute;
    left: 48px;
    top: 104px;
    width: 330px;
    margin: 0;
    font-size: 18px;
    line-height: 22px;
    color: var(--ink);
  }
  .headline {
    position: absolute;
    margin: 0;
    font-weight: 300;
    white-space: nowrap;
  }
  .lead {
    left: 46px;
    top: 184px;
    font-size: 56px;
    line-height: 70px;
    color: var(--ink);
  }
  .audience {
    left: 46px;
    top: 376px;
    font-size: 68px;
    line-height: 86px;
    color: var(--brand-red);
  }
  .offer {
    right: 47px;
    top: 622px;
    text-align: right;
    font-size: 55px;
    line-height: 70px;
    color: var(--ink);
  }
  .condition {
    right: 47px;
    top: 811px;
    text-align: right;
    font-size: 70px;
    line-height: 88px;
    color: var(--brand-red);
  }
  .call-to-action {
    position: absolute;
    left: 48px;
    top: 1040px;
    margin: 0;
  }
  .call-to-action .shout {
    display: block;
    font-size: 34px;
    line-height: 44px;
    color: var(--brand-red);
  }
  .call-to-action .email {
    display: block;
    font-size: 26px;
    line-height: 38px;
    color: var(--ink);
  }
</style>
</head>
<body>
<main class="advert">
  <svg class="backdrop" viewBox="0 0 675 1200" xmlns="http://www.w3.org/2000/svg">
    <defs>
      <linearGradient id="photoTone" x1="0" y1="0" x2="1" y2="1">
        <stop offset="0" stop-color="var(--photo-light)"/>
        <stop offset="0.45" stop-color="var(--photo-mid)"/>
        <stop offset="1" stop-color="var(--photo-dark)"/>
      </linearGradient>
    </defs>
    <polygon class="panel-shade" points="0,320 490,262 675,472 675,1112" fill="var(--panel)"/>
    <polygon class="photo-area" role="img"
             aria-label="Photo of a smiling young woman in a white shirt in a bright office, a colleague working at a computer behind her"
             points="0,320 675,1112 675,1200 0,1200" fill="url(#photoTone)"/>
    <polygon class="photo-veil" points="180,530 675,470 675,1112" fill="var(--panel)" opacity="0.55"/>
    <polygon class="red-corner" points="276,0 675,0 675,472" fill="var(--brand-red)"/>
  </svg>

  <p class="web-address">www.kelvano.uk/ideas</p>
  <p class="brand-name">KELVANO</p>

  <p class="question">Do you have a business idea that would benefit with advertising on these screens?</p>

  <h1 class="headline lead">We want to<br>support</h1>
  <h2 class="headline audience">YOUNG<br>ENTERPRENEURS</h2>
  <p class="headline offer">and will partner<br>with any</p>
  <p class="headline condition">WHOM HAVE<br>A GREAT IDEA</p>

  <p class="call-to-action">
    <span class="shout">WE WANT TO HEAR FROM YOU!</span>
    <span class="email">Email us at ideas@kelvano.uk</span>
  </p>
</main>
</body>
</html>
```